New Design for Accounting Firm

CLIENT NAME: Corvantis
CURRENT WEBSITE: www.corvantisgroup-example.com.au

CLIENTS THE CLIENT LIKES:
http://velmarook.example.se/
http://www.tralvexio.example.biz/index.php
http://www.brindlequo.example.co.uk/
http://www.nerovaskellintrust.example.org/

COLOUR THEMES:
Colour theme to reflect the logo, with a leaning to blue in Accounting & Audit sections and green in Super section.

LOOK AND FEEL:
The look and feel needs to reflect an accessible culture and contemporary sensibility while still communicating our experience and stability as a professional company.

ABOUT:
The concept of 'Corvantis' is integral to our identity. Definition: 'The connection of creative ideas from a group of diverse individuals, applied with the end aim of solving practical problems'. See ''About Us'' on our website for more.

OTHER DETAILS:
Our three divisions (and service areas within each division) must be easily navigated as they related to very different users of the site. Two client sign in sections (Accounting & Super) must be easily distinguished to avoid user confusion.

MENU STRUCTURE:
* About
- includes history, values, our people, community etc
* Accounting & Advisory
- About
- Services
- Tax & Accounting
- Business Advisory
- Family Wealth Management
- Client Sign In
- Calculators
* Audit & Assurance
- About
- Services
* Corvantis Super
- About
- Individuals
- Services
- Advisers
- Services
- Portal Sign In
- Calculators
* Careers
* Newsletters
* Contact

REQUIREMENTS:
- Layered PSD form home and content pages
- No coding required, we use our own CMS to insert XHTML files into.
Updates

Hi Guys,

The client has asked for a non-cliche'd images in the design. If you'd like to try again with some images that represent the business but aren't your standard boring accounting-looking people, then please do! Cliche is a killer in design - please pump some creativity in!

Cheers,
Ted.

Reason: GUYS - PLEASE LISTEN TO THESE COMMENTS - I'VE SAID THEM TWICE NOW AND PEOPLE ARE STILL POSTING PROJECTS WITH CLICHED AND OBVIOUS ACCOUTNING TYPE IMAGES. USE YOUR CREATIVITY AND POST A DESIGN THAT IS OUTSIDE THE BOX WITH REGARDS TO THE IMAGES YOU ARE USING.

Reason: I am waiting to hear back from the client on their decision.

```html
<!DOCTYPE html>
<html lang="en">
<head>
<meta charset="utf-8">
<title>Corvantis – Welcome</title>
<link rel="stylesheet" href="https://fonts.googleapis.com/css2?family=Arimo:wght@400;700&display=swap">
<style>
:root{
  --blue:#1a6fb5;
  --blue-dark:#0f4f8c;
  --blue-light:#3f92d4;
  --green:#72c45e;
  --green-light:#a6e290;
  --link:#1768b0;
  --text:#333;
  --on-color:#ffffff;
  --grey-line:#d6d6d6;
  --bg:#ffffff;
}
*{box-sizing:border-box;margin:0;padding:0}
html,body{width:1200px;height:1170px;overflow:hidden;background:var(--bg);font-family:"Arimo",Arial,sans-serif;color:var(--text)}
.page{position:relative;width:1200px;height:1170px;background:linear-gradient(#ececec 0,#fafafa 60px,#fff 110px)}
.main-nav{position:absolute;top:58px;left:175px;display:flex;gap:3px}
.main-nav a{display:block;height:38px;padding-top:12px;text-align:center;font-size:12px;color:var(--link);text-decoration:none;background:linear-gradient(#fff,#f1f1f1);border:1px solid var(--grey-line);border-bottom:none;border-radius:8px 8px 0 0}
.header{position:absolute;top:96px;left:88px;width:1023px;height:86px;background:linear-gradient(90deg,#fff 30%,#f2f2f2);border-top:1px solid var(--grey-line)}
.brand{position:absolute;left:4px;top:8px;display:flex;align-items:center;gap:10px}
.brand-mark{width:54px;height:54px;background:var(--blue)}
.brand-name{font-size:58px;color:var(--blue);font-weight:400;letter-spacing:-1px}
.sign-in{position:absolute;top:19px;height:44px;border-radius:6px;color:var(--on-color);font-size:12px;font-weight:700;padding:15px 0 0 22px;box-shadow:0 2px 3px rgba(0,0,0,.25)}
.sign-in svg{position:absolute;right:14px;top:7px}
.sign-in--accounting{left:617px;width:180px;background:linear-gradient(var(--blue-light),var(--blue-dark))}
.sign-in--super{left:823px;width:181px;background:linear-gradient(var(--green-light),var(--green))}
.tagline{position:absolute;top:181px;left:88px;width:1023px;height:31px;background:linear-gradient(var(--blue-light),var(--blue-dark));border-radius:0 0 8px 8px;color:var(--on-color);font-size:11px;padding:8px 11px}
.hero{position:absolute;top:223px;left:88px;width:1023px;height:224px;border-radius:8px;overflow:hidden;background:linear-gradient(90deg,#f4f8fb 0,#cfe9f7 30%,#8fd0f2 60%,#3aa7e6 100%)}
.hero-caption{position:absolute;left:17px;bottom:7px;font-size:23px;font-weight:700;color:#fff;letter-spacing:-.3px;text-shadow:-1px -1px 0 #234,1px -1px 0 #234,-1px 1px 0 #234,1px 1px 0 #234,2px 2px 3px rgba(0,0,0,.5)}
.content{position:absolute;top:467px;left:88px;width:825px;font-size:12px;line-height:18px}
.page-title{display:flex;align-items:center;height:41px;border:1px solid var(--grey-line);border-radius:8px;background:linear-gradient(#fff,#ececec);font-size:27px;line-height:1;font-weight:400;padding:2px 17px 0;margin-right:10px;box-shadow:0 2px 2px rgba(0,0,0,.1)}
.content p{padding-left:3px;margin-top:18px}
.content p.lead{margin-top:17px}
.content a{color:var(--link);text-decoration:none}
.divisions{display:flex;gap:21px;margin:10px 0 0 5px}
.content .division{display:block;height:44px;border-radius:8px;color:var(--on-color);font-size:12px;font-weight:700;text-align:center;padding-top:13px;box-shadow:0 2px 3px rgba(0,0,0,.25);text-shadow:0 1px 1px rgba(0,0,0,.25)}
.content .division--accounting{width:245px;background:linear-gradient(var(--blue-light),var(--blue-dark))}
.content .division--audit{width:246px;background:linear-gradient(var(--blue-light),var(--blue-dark))}
.content .division--super{width:181px;background:linear-gradient(var(--green-light),var(--green))}
.ticks{list-style:none;margin:24px 0 0 9px}
.ticks li{display:flex;align-items:center;gap:9px;height:24px}
.enquiry{position:absolute;top:467px;left:932px;width:180px;height:273px;border:1px solid var(--grey-line);border-radius:8px;background:#f1f1f1;overflow:hidden}
.enquiry-art{position:absolute;top:12px;left:12px;width:155px;height:171px;border-radius:8px;background:#fff;box-shadow:0 1px 3px rgba(0,0,0,.2)}
.enquiry-art span{position:absolute;left:20px;top:26px;width:113px;height:117px;border-radius:50%;background:radial-gradient(#e4fbd8,#9fe35a)}
.enquiry-label{position:absolute;bottom:0;left:0;width:100%;height:76px;background:linear-gradient(var(--blue),var(--blue-dark));color:var(--on-color);padding:18px 0 0 23px}
.enquiry-label small{display:block;font-size:13px;font-weight:700}
.enquiry-label strong{display:block;font-size:18px;margin-top:2px}
.footer{position:absolute;top:1108px;left:88px;width:1023px;height:44px;border:1px solid var(--grey-line);border-radius:8px;background:linear-gradient(#fff,#e8e8e8);font-size:11px;padding:14px 20px;display:flex;justify-content:space-between}
.footer nav a{color:var(--text);text-decoration:none}
</style>
</head>
<body>
<div class="page">
  <nav class="main-nav">
    <a href="#" style="width:114px">About</a>
    <a href="#" style="width:174px">Accounting &amp; Advisory</a>
    <a href="#" style="width:174px">Audit &amp; Assurance</a>
    <a href="#" style="width:114px">Corvantis Super</a>
    <a href="#" style="width:114px">Careers</a>
    <a href="#" style="width:114px">Newsletters</a>
    <a href="#" style="width:114px">Contact</a>
  </nav>

  <header class="header">
    <div class="brand"><span class="brand-mark"></span><span class="brand-name">Corvantis</span></div>
    <a class="sign-in sign-in--accounting">Accounting Sign In
      <svg width="32" height="30" viewBox="0 0 32 30"><rect x="12" y="1" width="16" height="28" fill="#fff" stroke="#cfe" /><path d="M2 17h14M11 12l5 5-5 5" stroke="#8fe6f2" stroke-width="3" fill="none"/></svg></a>
    <a class="sign-in sign-in--super">Super Sign In
      <svg width="32" height="30" viewBox="0 0 32 30"><rect x="12" y="1" width="16" height="28" fill="#fff" stroke="#cfe" /><path d="M2 17h14M11 12l5 5-5 5" stroke="#5fe0c0" stroke-width="3" fill="none"/></svg></a>
  </header>
  <div class="tagline">Corvantis is a multi-faceted financial services firm, incorporating the skills of accountants, business advisers, auditors and SMSF specialists</div>

  <div class="hero" role="img" aria-label="Banner illustration: coloured bar chart with rising arrow, world map and silhouettes of business people">
    <div class="hero-caption">Accounting and Tax Audit and Assurance Self Managed Super</div>
  </div>

  <main class="content">
    <h1 class="page-title">Welcome</h1>
    <p class="lead">Corvantis is a Tasmanian based firm which offers the skills of Accountants, Business Performance Advisers, Auditors and Self Managed Super Fund Specialists.</p>
    <p>From our offices in Devonport and Hobart we deliver services across three divisions:</p>
    <div class="divisions">
      <a href="#" class="division division--accounting">AG Corvantis Chartered Accountants</a>
      <a href="#" class="division division--audit">Corvantis Audit &amp; Assurance</a>
      <a href="#" class="division division--super">Corvantis Super</a>
    </div>
    <p>Through our three divisions, our clients benefit from the application of specialist skills and systems, developed in relevant areas of expertise. At the same time, our teams are skilled at integrating their knowledge with the common goal of meeting our clients' comprehensive needs.</p>
    <p>Across the firm we deliver services in a wide range of industries; to individuals, businesses, corporations and financial advisers. Our services include:</p>
    <ul class="ticks">
      <li><svg width="15" height="12"><path d="M1 6l4 4 9-9" stroke="#5cb83c" stroke-width="3" fill="none"/></svg> Accounting and Taxation</li>
      <li><svg width="15" height="12"><path d="M1 6l4 4 9-9" stroke="#5cb83c" stroke-width="3" fill="none"/></svg> Corporate and Business Advice</li>
      <li><svg width="15" height="12"><path d="M1 6l4 4 9-9" stroke="#5cb83c" stroke-width="3" fill="none"/></svg> Family Wealth Management</li>
      <li><svg width="15" height="12"><path d="M1 6l4 4 9-9" stroke="#5cb83c" stroke-width="3" fill="none"/></svg> Audit and Assurance</li>
      <li><svg width="15" height="12"><path d="M1 6l4 4 9-9" stroke="#5cb83c" stroke-width="3" fill="none"/></svg> Self Managed Super Fund Administration</li>
    </ul>
    <p style="margin-top:12px">We offer peace of mind regarding the cost and delivery of our services with a committment to:</p>
    <ul class="ticks" style="margin-top:20px">
      <li><svg width="15" height="12"><path d="M1 6l4 4 9-9" stroke="#5cb83c" stroke-width="3" fill="none"/></svg> <a href="#">Quoted Upfront Fees</a></li>
      <li><svg width="15" height="12"><path d="M1 6l4 4 9-9" stroke="#5cb83c" stroke-width="3" fill="none"/></svg> <a href="#">Guaranteed Turnaround Times</a></li>
      <li><svg width="15" height="12"><path d="M1 6l4 4 9-9" stroke="#5cb83c" stroke-width="3" fill="none"/></svg> <a href="#">Integrated Service Plans</a></li>
    </ul>
    <p style="margin-top:14px">We strive to surpass the expectations you might have of traditional accounting firms. The strength of our client relationships is evidence that we consis-tently deliver to that standard.</p>
    <p>If you are ready to change to a better way of looking at your accounting, tax, business, audit or self managed super fund needs, <a href="#">contact us</a>.</p>
  </main>

  <aside class="enquiry">
    <div class="enquiry-art" role="img" aria-label="Envelope and pointer icon on a green splash"><span></span></div>
    <div class="enquiry-label"><small>click here for</small><strong>ENQUIRY FORM</strong></div>
  </aside>

  <footer class="footer">
    <span>© 2011 Corvantis Group</span>
    <nav><a href="#">Home</a> &nbsp;|&nbsp; <a href="#">Privacy</a> &nbsp;|&nbsp; <a href="#">Contact</a></nav>
  </footer>
</div>
</body>
</html>
```